Faris Methani Business Card

I would like an elegant business card design in both english and arabic.

Ideally a logo design with my name in Arabic (could be a tiger for example)

It should have my Name : Faris Methani
Title: Advisor / Investor
Tel. UAE +971 558 274 903
UK +44 7821 560 287
Email. farmethani412@mailvane.net

I am an active angle investor and have many business interests in the TMT space and invest globally, the design needs to be fresh, elegant and striking.

The design should be catching and grab one's attention when they view the card.

Front card should be in English and Reverse in Arabic....

Target Market(s)

Global Investors, CEO's

Industry/Entity Type

Business

Contact Information for Business Card

Title: Advisor / Investor
Tel. UAE +971 558 274 903
UK +44 7821 560 287

Font styles to use
Serif
Other font styles liked:
• Palantino

Requirements
Must have
• A striking design with a play of my name in Arabic, could be my name that is designed as a tiger for example

```html
<!DOCTYPE html>
<html lang="en">
<head>
<meta charset="utf-8">
<title>Faris Methani – Business Card</title>
<link href="https://fonts.googleapis.com/css2?family=Tinos:wght@400;700&family=Noto+Naskh+Arabic:wght@400;700&display=swap" rel="stylesheet">
<style>
  :root {
    --paper: #ffffff;
    --ink: #111111;
    --rule: #222222;
    --tiger-dark: #2a2a2a;
    --tiger-light: #d9d9d9;
  }
  * { margin: 0; padding: 0; box-sizing: border-box; }
  html, body {
    width: 1200px;
    height: 402px;
    overflow: hidden;
    background: var(--paper);
  }
  .canvas {
    position: relative;
    width: 1200px;
    height: 402px;
    background: var(--paper);
    color: var(--ink);
  }
  .card {
    position: absolute;
    top: 24px;
    height: 351px;
    border: 1.5px solid var(--rule);
    background: var(--paper);
  }
  .card--front { left: 24px; width: 573px; }
  .card--back { left: 627px; width: 546px; }

  .tiger-mark {
    position: absolute;
    border-radius: 45% 40% 45% 50%;
    background: radial-gradient(circle at 45% 45%, var(--tiger-light) 0%, #8a8a8a 45%, var(--tiger-dark) 100%);
  }
  .card--front .tiger-mark { left: 424px; top: 118px; width: 102px; height: 104px; }
  .card--back .tiger-mark { left: 373px; top: 105px; width: 150px; height: 112px; }

  .name-en {
    position: absolute;
    right: 150px;
    top: 146px;
    font-family: "Tinos", "Times New Roman", serif;
    font-weight: 700;
    font-size: 44px;
    letter-spacing: 0.5px;
    line-height: 1;
    white-space: nowrap;
  }
  .title-en {
    position: absolute;
    right: 160px;
    top: 198px;
    font-family: "Tinos", "Times New Roman", serif;
    font-size: 14px;
    line-height: 1;
  }
  .contacts {
    position: absolute;
    right: 38px;
    top: 288px;
    text-align: right;
    font-family: "Tinos", "Times New Roman", serif;
    font-size: 15px;
    line-height: 25px;
  }

  .name-ar {
    position: absolute;
    right: 172px;
    top: 82px;
    direction: rtl;
    font-family: "Noto Naskh Arabic", serif;
    font-weight: 700;
    font-size: 66px;
    line-height: 1.2;
    white-space: nowrap;
  }
  .title-ar {
    position: absolute;
    right: 178px;
    top: 188px;
    direction: rtl;
    font-family: "Noto Naskh Arabic", serif;
    font-size: 34px;
    line-height: 1.2;
    white-space: nowrap;
  }
  .email {
    position: absolute;
    right: 30px;
    top: 318px;
    font-family: "Tinos", "Times New Roman", serif;
    font-size: 15px;
    line-height: 1;
  }
</style>
</head>
<body>
<main class="canvas">
  <section class="card card--front" aria-label="Front of card, English">
    <div class="tiger-mark" role="img" aria-label="Roaring tiger head illustration in black line work"></div>
    <h1 class="name-en">FARIS METHANI</h1>
    <p class="title-en">Advisor / Investor</p>
    <p class="contacts">
      UAE + 971 558 274 903<br>
      UK + 44 7821 560 287
    </p>
  </section>

  <section class="card card--back" aria-label="Back of card, Arabic" lang="ar">
    <div class="tiger-mark" role="img" aria-label="Roaring tiger head illustration in black line work"></div>
    <h2 class="name-ar">فارس ميثاني</h2>
    <p class="title-ar">مستثمر / المستشار</p>
    <p class="email" lang="en">farmethani412@mailvane.net</p>
  </section>
</main>
</body>
</html>
```